E-Commerce Website Update for Bamboo Poles Company

Existing website at:

http://www.reedcraftstudio.example/
http://www.reedcraftstudio.example/pages/product-and-price-list

Two pages to design: home page and "price list" page.

Info for home page as follows:

HOME PAGE:

Header:
Company Name: reedcraft studio
Telephone: 1 888 412 5093

Across the top:
Home | Price List | Blog | FAQ | About | Contact

Down the side:
About Bamboo
Wedding Arbors
Bamboo For Flutes
Black Bamboo
Spotted Bamboo
Bamboo Carpentry
Photo Gallery
All Products & Prices
Blog
FAQ
About
Contact

Should have shopping cart and search buttons on top.
Please see ai file, attached for logo (leaf) and font
In addition the homepage should have one or two sections for promotions

Chosen design will be asked to help deign a PRODUCT AND PRICE LIST page similar to the one we have now, but with "LEARN MORE" and "ORDER NOW" buttons for each item.
Updates

Reason: Thanks  for all the designs so far; giving an extra week for extra consideration.

Target Market(s)

Consumers, wedding planners.

Industry/Entity Type

Shopping

Requirements
Must have
• Clean, easy to read design.
Should not have
• No flash animation.

```html
<!DOCTYPE html>
<html lang="en">
<head>
<meta charset="utf-8">
<title>reedcraft studio — Home</title>
<link href="https://fonts.googleapis.com/css2?family=Arimo:wght@400;700&display=swap" rel="stylesheet">
<style>
:root{
  --green:#127a2c;
  --green-dark:#0f6a27;
  --green-text:#137a2c;
  --ink:#1a1a1a;
  --body:#444;
  --panel:#fff;
  --side:#2b2b2b;
  --rule:#cfcfcf;
  --promo:#eef6ea;
}
*{box-sizing:border-box;margin:0;padding:0}
html,body{width:1089px;height:1200px;overflow:hidden}
body{position:relative;font-family:"Arimo",Arial,sans-serif;color:var(--ink)}
.forest{position:absolute;inset:0;background:radial-gradient(ellipse at 50% 40%,#d9efcf 0%,#8cc27a 40%,#3f8a3a 75%,#255f27 100%)}
.header{position:absolute;left:22px;top:25px;width:1048px;height:71px;background:linear-gradient(#47ad32,#1f8a22 60%,#167a1f);border-bottom:4px solid #1c3a1c}
.brand{position:absolute;left:12px;top:4px;color:#fff;font-size:34px;line-height:30px;font-weight:700;letter-spacing:-0.5px;width:200px}
.brand span{display:block;font-size:27px}
.mainnav{position:absolute;left:281px;top:19px;display:flex}
.mainnav a{color:#fff;text-decoration:none;font-size:20px;padding:9px 12px;height:46px;line-height:28px}
.mainnav a.active{background:#2c5e3f}
.tools{position:absolute;right:28px;top:14px;display:flex;gap:18px;color:#fff}
.tool{display:flex;gap:8px}
.tool svg{width:27px;height:27px}
.tool b{display:block;font-weight:400;font-size:19px;line-height:19px}
.tool small{display:block;font-size:10px;font-weight:700}
.hero{position:absolute;left:22px;top:99px;width:450px;height:490px;border-radius:0 0 0 14px;background:linear-gradient(90deg,#2d6b4a,#7fb89a 25%,#3f8063 45%,#9ac8ae 60%,#2e6a4c 80%,#173d2a)}
.welcome{position:absolute;left:472px;top:99px;width:597px;height:490px;background:var(--panel);border-radius:0 0 14px 0;padding:24px 21px 0 27px;color:var(--body);font-size:14px;line-height:20.4px;text-align:justify}
.welcome h1{font-weight:400;color:#111;font-size:26px;line-height:30px;text-align:left}
.promos{position:absolute;left:27px;right:21px;bottom:18px;display:flex;gap:14px}
.promo{flex:1;background:var(--promo);border-left:4px solid var(--green);padding:10px 12px;text-align:left}
.promo h4{color:var(--green-text);font-size:15px;font-weight:700;line-height:18px}
.promo p{font-size:12px;line-height:16px;margin-top:3px}
.sidebar{position:absolute;left:22px;top:600px;width:239px;height:489px;background:var(--side);border-radius:14px 0 0 14px;overflow:hidden}
.sidebar h2{background:var(--green);color:#fff;font-weight:400;font-size:24px;height:51px;line-height:51px;padding-left:27px}
.sidebar ul{list-style:none;margin-top:17px}
.sidebar li{margin-left:30px;width:146px;border-bottom:1px dotted #2d7a3a;height:34px;line-height:30px}
.sidebar a{color:#fff;text-decoration:none;font-size:13px}
.grid{position:absolute;left:261px;top:600px;width:808px;height:489px;background:var(--panel);border-radius:0 14px 14px 0;display:grid;grid-template-columns:196px 197px 196px 219px;grid-template-rows:241px 248px;overflow:hidden}
.item{border-right:1px solid var(--rule);border-bottom:1px solid var(--rule);display:flex;flex-direction:column;align-items:center;padding:18px 10px 10px;color:var(--green-text)}
.item:nth-child(4n){border-right:0}
.item:nth-child(n+5){border-bottom:0}
.item h3{font-weight:400;font-size:16px;align-self:flex-start;margin-left:10px}
.item .num{font-size:12px;align-self:flex-start;margin:10px 0 10px 10px}
.item .pic{width:92px;height:82px}
.item .price{font-size:12px;margin:10px 0 auto}
.btn{background:var(--green);color:#fff;font-size:13px;text-decoration:none;width:88px;height:35px;line-height:35px;text-align:center;border-radius:4px}
.cane{background:linear-gradient(90deg,#c9bf8a,#e2d7a6 30%,#b8ad72 60%,#d8cd98)}
.black{background:linear-gradient(90deg,#3a302b,#6a5d55 30%,#2b2320 60%,#5a4c44)}
.spot{background:linear-gradient(90deg,#5b4d3f,#8c7a63 30%,#4a3d30 60%,#7c6a52)}
.arbor{background:linear-gradient(#f3f3ef,#e3ddc8)}
.footer{position:absolute;left:22px;top:1100px;width:1048px;height:100px;background:var(--green-dark);border-radius:12px 12px 0 0;color:#fff;font-size:11px;padding:11px 14px;line-height:14px}
.footer p+p{margin-top:19px}
</style>
</head>
<body>
<div class="forest" role="img" aria-label="Bamboo forest backdrop"></div>

<header class="header">
  <div class="brand">reedcraft<span>studio</span></div>
  <nav class="mainnav">
    <a class="active" href="#">Home</a><a href="#">Price List</a><a href="#">Blog</a><a href="#">FAQ</a><a href="#">About</a><a href="#">Contact</a>
  </nav>
  <div class="tools">
    <div class="tool">
      <svg viewBox="0 0 27 27"><rect width="27" height="27" fill="#3a3a3a"/><circle cx="12" cy="12" r="5.5" fill="none" stroke="#fff" stroke-width="1.8"/><path d="M16 16l5 5" stroke="#fff" stroke-width="2"/></svg>
      <div><b>Search</b><small>Find Poles</small></div>
    </div>
    <div class="tool">
      <svg viewBox="0 0 27 27"><rect width="27" height="27" fill="#3a3a3a"/><path d="M4 7h3l2 9h11l2-7H8" fill="none" stroke="#fff" stroke-width="1.6"/><circle cx="11" cy="20" r="1.6" fill="#fff"/><circle cx="18" cy="20" r="1.6" fill="#fff"/></svg>
      <div><b>Cart</b><small>Shopping Cart</small></div>
    </div>
  </div>
</header>

<div class="hero" role="img" aria-label="Photograph of tall green bamboo stalks"></div>

<section class="welcome">
  <h1>Welcome to your Pole Provider 1 888 412 5093</h1>
  <p>Bamboo poles at wholesale prices direct from reedcraft studio.</p>
  <p>Need bamboo poles at a competitive price? Welcome to your one-stop pole shop. We warehouse a variety of types poles in a variety of diameters, from 5/8" to 5 1/2", in lengths up to 8’. We have natural poles, moso (mao) timber poles, black poles spotted poles… and regular bamboo poles. Whatever your project may be, from flutes to weddings to roasting a pig, we have the perfect pole for you.</p>
  <p>Poles are warehoused in Los Angeles, and ready for immediate shipping by ParcelLine ground to all of the United States. Or, if you’re in the SoCal area, you can collect your poles at our warehouse (see our FAQs).</p>
  <p>For our complete list of products with prices, please click here.</p>
  <p>Take advantage of our online shop for easy ordering. If you have any questions, contact us by calling us anytime at 1.888.412.5093 or email us at orders@reedcraftstudio.example.</p>
  <p>If you prefer to purchase our poles through marketbay, or want to see feedback information about our product, please visit our marketbay site here.</p>
  <div class="promos">
    <div class="promo"><h4>Wedding Arbor Special</h4><p>Save 10% on arbors booked this month.</p></div>
    <div class="promo"><h4>Free Warehouse Pickup</h4><p>Collect your order in Los Angeles.</p></div>
  </div>
</section>

<aside class="sidebar">
  <h2>Navigation</h2>
  <ul>
    <li><a href="#">About Bamboo</a></li>
    <li><a href="#">Wedding Arbors</a></li>
    <li><a href="#">Bamboo For Flutes</a></li>
    <li><a href="#">Black Bamboo</a></li>
    <li><a href="#">Spotted Bamboo</a></li>
    <li><a href="#">Bamboo Carpentry</a></li>
    <li><a href="#">Photo Gallery</a></li>
    <li><a href="#">All Products &amp; Prices</a></li>
    <li><a href="#">Blog</a></li>
    <li><a href="#">FAQ</a></li>
    <li><a href="#">About</a></li>
    <li><a href="#">Contact</a></li>
  </ul>
</aside>

<main class="grid">
  <div class="item"><h3>Bamboo Poles</h3><span class="num">Item nunber: c1</span><div class="pic cane" role="img" aria-label="Natural bamboo poles"></div><span class="price">$ 1</span><a class="btn" href="#">DETAILS</a></div>
  <div class="item"><h3>Black Poles</h3><span class="num">Item nunber: c1</span><div class="pic black" role="img" aria-label="Black bamboo poles"></div><span class="price">$ 1</span><a class="btn" href="#">DETAILS</a></div>
  <div class="item"><h3>Spotted Poles</h3><span class="num">Item nunber: c1</span><div class="pic spot" role="img" aria-label="Spotted bamboo poles"></div><span class="price">$ 1</span><a class="btn" href="#">DETAILS</a></div>
  <div class="item"><h3>Bamboo Wedding Arbors</h3><span class="num">Item nunber: c1</span><div class="pic arbor" role="img" aria-label="Bamboo wedding arbor"></div><span class="price">$ 1</span><a class="btn" href="#">DETAILS</a></div>
  <div class="item"><span class="num">Item nunber: c1</span><div class="pic cane" role="img" aria-label="Thick natural bamboo poles"></div><span class="price">$ 1</span><a class="btn" href="#">DETAILS</a></div>
  <div class="item"><span class="num">Item nunber: c1</span><div class="pic black" role="img" aria-label="Black bamboo poles"></div><span class="price">$ 1</span><a class="btn" href="#">DETAILS</a></div>
  <div class="item"><span class="num">Item nunber: c1</span><div class="pic spot" role="img" aria-label="Spotted bamboo poles"></div><span class="price">$ 1</span><a class="btn" href="#">DETAILS</a></div>
  <div class="item"><span class="num">Item nunber: c1</span><div class="pic arbor" role="img" aria-label="Bamboo wedding arbor"></div><span class="price">$ 1</span><a class="btn" href="#">DETAILS</a></div>
</main>

<footer class="footer">
  <p>Copyright © 2011 reedcraft studio. All Rights Reserved. All prices USD.</p>
  <p>Powered by Shopwell.</p>
</footer>
</body>
</html>
```